Post storm repair flyer

looking for an eye catching 6x9 postcard to send out to single family home owners advertising a "Post Storm Repair Special" explaining that after the recent hurricanes its very important to have your roof checked and any repairs fixed right away before they become a bigger more costly problem and that even though your home wasn't directly hit by the storm the high wind gust could've cause unseen damage.
offer $200 off any repair *some rules may apply
Lark Roofing
888.417.LARK
www.LarkRoofing.example

Roofing

```html
<!DOCTYPE html>
<html lang="en">
<head>
<meta charset="utf-8">
<title>Lark Roofing – Post-Storm Roof Repair Special Postcard</title>
<link rel="stylesheet" href="https://fonts.googleapis.com/css2?family=Anton&family=Montserrat:wght@400;500;700;800;900&display=swap">
<style>
  :root{
    --bg:#d3d4d6;
    --gold:#e6b022;
    --black:#000;
    --white:#fff;
    --storm-dark:#1f3a45;
    --storm-mid:#587c86;
    --storm-light:#b9c9c9;
    --ink:#111;
  }
  *{box-sizing:border-box;margin:0;padding:0}
  html,body{width:1073px;height:1200px;overflow:hidden;background:var(--bg)}
  body{position:relative;font-family:"Montserrat",sans-serif;color:var(--ink)}
  .card{position:absolute;left:145px;width:784px;height:522px;background:var(--white);box-shadow:0 3px 8px rgba(0,0,0,.35);overflow:hidden}
  .card--front{top:53px}
  .card--back{top:610px}

  /* FRONT */
  .hero-photo{position:absolute;left:0;top:0;width:784px;height:297px;
    background:linear-gradient(115deg,var(--storm-dark) 0%,#2f5561 35%,var(--storm-mid) 60%,var(--storm-light) 100%)}
  .headline{position:absolute;left:29px;top:24px;color:var(--white);font-weight:800;font-size:73px;line-height:62px;letter-spacing:-1px;text-shadow:0 2px 6px rgba(0,0,0,.35)}
  .brand{position:absolute;left:684px;top:58px;transform:translateX(-50%);text-align:center;font-weight:500;font-size:13px;color:var(--ink);white-space:nowrap}
  .brand-mark{display:block;width:64px;height:64px;border:4px solid var(--black);margin:0 auto 18px}
  .alert-band{position:absolute;left:0;top:223px;width:512px;height:49px;background:var(--gold);padding:7px 0 0 30px;font-size:13.6px;line-height:17.5px;font-weight:500}
  .pitch{position:absolute;left:30px;top:322px;width:440px;font-size:20.5px;line-height:26.5px;font-weight:500}
  .pitch strong{color:var(--gold);font-weight:800}
  .fine-strip{position:absolute;left:0;top:420px;width:784px;height:31px;background:var(--black);color:var(--white);font-size:10.4px;padding:9px 0 0 30px;font-weight:500}
  .fine-strip b{font-weight:800}
  .offer-arrow{position:absolute;left:496px;top:324px}
  .offer-badge{position:absolute;left:512px;top:281px;width:248px;height:165px;background:var(--black);padding:6px}
  .offer-badge__inner{width:100%;height:100%;border:4px solid var(--white);background:var(--black);text-align:center;padding-top:14px}
  .offer-amount{font-family:"Anton",sans-serif;color:var(--gold);font-size:84px;line-height:82px}
  .offer-label{font-family:"Anton",sans-serif;color:var(--white);font-size:25px;line-height:28px}
  .contact-bar{position:absolute;left:0;top:458px;width:784px;height:64px;background:var(--gold)}
  .call{position:absolute;left:33px;top:14px;font-size:26px;font-weight:500;white-space:nowrap}
  .call b{font-weight:800;font-size:32px;letter-spacing:-.3px}
  .divider{position:absolute;left:431px;top:12px;width:2px;height:41px;background:var(--black)}
  .visit{position:absolute;left:458px;top:22px;font-size:11.5px;font-weight:500;white-space:nowrap}
  .visit span{font-size:16.5px;letter-spacing:.1px}

  /* BACK */
  .back-panel{position:absolute;left:0;top:0;width:379px;height:322px;
    background:linear-gradient(160deg,#ecb936 0%,var(--gold) 55%,#d9a624 100%)}
  .back-brand{position:absolute;left:184px;top:22px;transform:translateX(-50%);text-align:center;font-weight:500;font-size:13px;white-space:nowrap}
  .back-brand .brand-mark{width:64px;height:64px;margin-bottom:40px}
  .back-pitch{position:absolute;left:0;top:181px;width:379px;text-align:center;font-size:21px;line-height:26.5px;font-weight:500;white-space:nowrap}
  .back-offer{position:absolute;left:0;top:322px;width:379px;height:98px;background:var(--white)}
  .back-offer .amount{position:absolute;left:41px;top:4px;font-family:"Anton",sans-serif;color:var(--gold);font-size:84px;line-height:90px}
  .back-offer .label{position:absolute;left:210px;top:10px;font-family:"Anton",sans-serif;font-size:39px;line-height:39px}
  .back-contact{position:absolute;left:0;top:420px;width:379px;height:102px;background:var(--black);padding:12px 0 0 42px}
  .back-contact .phone{color:var(--gold);font-weight:800;font-size:37px;line-height:40px;letter-spacing:-.5px}
  .back-contact .url{color:var(--white);font-weight:500;font-size:19px;line-height:26px;margin-left:2px}
  .stamp-box{position:absolute;left:614px;top:41px;width:132px;height:147px;border:1px solid #333}
  .address-line{position:absolute;left:392px;width:277px;height:1px;background:#555}
</style>
</head>
<body>

<section class="card card--front" aria-label="Postcard front">
  <div class="hero-photo" role="img" aria-label="Photo of a storm-damaged house roof under dark storm clouds"></div>
  <h1 class="headline">POST-STORM<br>ROOF REPAIR<br>SPECIAL!</h1>
  <div class="brand"><span class="brand-mark"></span>LARKROOFING.EXAMPLE</div>
  <p class="alert-band">Recent storms can cause hidden damage to your roof.<br>Don't wait until it's too late—get a professional inspection today!</p>
  <p class="pitch"><strong>PROTECT YOUR HOME</strong> and avoid costly<br>repairs by addressing storm damage<br>early. Our expert team is ready to help!</p>
  <p class="fine-strip">OFFER INCLUDES A FREE INSPECTION AND <b>$200 OFF</b> ANY QUALIFYING REPAIR.*</p>
  <svg class="offer-arrow" width="30" height="96" viewBox="0 0 30 96" aria-hidden="true"><polygon points="0,0 30,35 30,70 4,96 22,48" fill="#000"/></svg>
  <div class="offer-badge">
    <div class="offer-badge__inner">
      <div class="offer-amount">$200</div>
      <div class="offer-label">OFF ANY REPAIR</div>
    </div>
  </div>
  <div class="contact-bar">
    <p class="call">Call now: <b>888.417.LARK</b></p>
    <span class="divider"></span>
    <p class="visit">Visit us at: <span>www.LarkRoofing.example</span></p>
  </div>
</section>

<section class="card card--back" aria-label="Postcard back">
  <div class="back-panel" role="img" aria-label="Faint gold-tinted photo of a damaged roof"></div>
  <div class="back-brand"><span class="brand-mark"></span>LARKROOFING.EXAMPLE</div>
  <p class="back-pitch">Protect your home and avoid<br>costly repairs by addressing<br>storm damage early. Our<br>expert team is ready to help!</p>
  <div class="back-offer">
    <span class="amount">$200</span>
    <span class="label">OFF ANY<br>REPAIR</span>
  </div>
  <div class="back-contact">
    <p class="phone">888.417.LARK</p>
    <p class="url">www.LarkRoofing.example</p>
  </div>
  <div class="stamp-box"></div>
  <span class="address-line" style="top:322px"></span>
  <span class="address-line" style="top:369px"></span>
  <span class="address-line" style="top:416px"></span>
  <span class="address-line" style="top:463px"></span>
</section>

</body>
</html>
```